CD-/Plattencover für Tonträgerfirma
Zielgruppe
Wir sind eine Tonträgerfirma und bewegen uns im Low-Budget-Segment.
Aufgabenstellung
Für eine KLassik Serie benötigen wir 7 Cover, welche aber im Grundlayout immer gleich seinen sollten. Es soll eine erkenntliche Serie entstehen.
Das Thema lautet: Velvet Hour
Die Unterthemen lauten:
1. The Amber Lantern Gathering
2. The Velvet Hour Riverside Suites
3. The Velvet Hour Meadow Steps
4. The Velvet Hour Moonlit Whispers
5. The Copper Table Evenings
6. The Silver Curtain Soirée
7. The Northwind Orchestral Treasures
Wir benötigen nicht das komplette Artwork, sondern ein Frontcover
(12 x 12 cm + 2 cm Beschnitt wg. etwaiger Verschiebung der Positionierung
Fertigstellung (Aufziehen des Inlays und Labels) erfolgt später bei uns im Hause
Wir benötigen später offene psd-Dateien mit allen Ebenen
Wichtig: Schriften nicht gerastert ggfs. Schrift mitliefern

```html
<!DOCTYPE html>
<html lang="en">
<head>
<meta charset="utf-8">
<title>Velvet Hour – Cover Series</title>
<link rel="stylesheet" href="https://fonts.googleapis.com/css2?family=Dancing+Script:wght@500&family=Lato:wght@400&display=swap">
<style>
  :root {
    --page: #ffffff;
    --ink: #ffffff;
    --amber-a: #bd1622; --amber-b: #d8441c; --amber-c: #f08a00; --amber-ring: #d63c1d;
    --river-a: #ea7322; --river-b: #f2a01e; --river-c: #ffe600; --river-ring: #e38020;
    --meadow-a: #ffe600; --meadow-b: #8fb52e; --meadow-c: #12903a; --meadow-ring: #789234;
    --moon-a: #1a8f3e; --moon-b: #2e9c8a; --moon-c: #30a8e0; --moon-ring: #12788f;
    --copper-a: #2fa9e1; --copper-b: #2f6cb0; --copper-c: #2e2a7c; --copper-ring: #163f86;
    --silver-a: #33287c; --silver-b: #62287f; --silver-c: #932181; --silver-ring: #3e2a68;
    --north-a: #9b2179; --north-b: #b01e52; --north-c: #bd1a28; --north-ring: #ad1e3a;
  }
  * { margin: 0; padding: 0; box-sizing: border-box; }
  html, body { width: 849px; height: 1200px; overflow: hidden; background: var(--page); }
  .sheet { position: relative; width: 849px; height: 1200px; }

  .cover {
    position: absolute;
    width: var(--size);
    height: var(--size);
    background: linear-gradient(45deg, var(--a), var(--b) 50%, var(--c));
    box-shadow: 2px 3px 4px rgba(0,0,0,0.18);
    overflow: hidden;
    color: var(--ink);
  }
  .cover__ring {
    position: absolute;
    left: 50%; top: 50%;
    width: 55%; height: 55%;
    transform: translate(-50%, -50%);
    border: 1px solid var(--ink);
    border-radius: 50%;
    background: var(--ring);
  }
  .cover__title {
    position: absolute;
    left: 0; right: 0; top: 50%;
    transform: translateY(-50%);
    text-align: center;
  }
  .cover__series {
    display: block;
    font-family: 'Lato', sans-serif;
    font-size: calc(var(--size) * 0.04);
    text-align: left;
    padding-left: 30%;
    margin-bottom: calc(var(--size) * -0.03);
  }
  .cover__name {
    display: block;
    font-family: 'Dancing Script', cursive;
    font-weight: 500;
    font-size: calc(var(--size) * 0.125);
    line-height: 1.2;
    white-space: nowrap;
  }
  .cover--lead { --size: 303px; left: 273px; top: 171px; }

  .cover--amber  { --a: var(--amber-a);  --b: var(--amber-b);  --c: var(--amber-c);  --ring: var(--amber-ring); }
  .cover--river  { --a: var(--river-a);  --b: var(--river-b);  --c: var(--river-c);  --ring: var(--river-ring); }
  .cover--meadow { --a: var(--meadow-a); --b: var(--meadow-b); --c: var(--meadow-c); --ring: var(--meadow-ring); }
  .cover--moon   { --a: var(--moon-a);   --b: var(--moon-b);   --c: var(--moon-c);   --ring: var(--moon-ring); }
  .cover--copper { --a: var(--copper-a); --b: var(--copper-b); --c: var(--copper-c); --ring: var(--copper-ring); }
  .cover--silver { --a: var(--silver-a); --b: var(--silver-b); --c: var(--silver-c); --ring: var(--silver-ring); }
  .cover--north  { --a: var(--north-a);  --b: var(--north-b);  --c: var(--north-c);  --ring: var(--north-ring); }

  .cover--grid { --size: 238px; }
  .col-1 { left: 25px; } .col-2 { left: 304px; } .col-3 { left: 584px; }
  .row-1 { top: 574px; } .row-2 { top: 853px; }
  .cover--grid .cover__name { font-size: 27px; }
</style>
</head>
<body>
<main class="sheet">
  <section class="cover cover--lead cover--amber">
    <div class="cover__ring"></div>
    <h1 class="cover__title"><span class="cover__series">The Amber</span><span class="cover__name">Lantern Gathering</span></h1>
  </section>

  <section class="cover cover--grid cover--river col-1 row-1">
    <div class="cover__ring"></div>
    <h2 class="cover__title"><span class="cover__series">The Velvet Hour</span><span class="cover__name">Riverside Suites</span></h2>
  </section>
  <section class="cover cover--grid cover--meadow col-2 row-1">
    <div class="cover__ring"></div>
    <h2 class="cover__title"><span class="cover__series">The Velvet Hour</span><span class="cover__name">Meadow Steps</span></h2>
  </section>
  <section class="cover cover--grid cover--moon col-3 row-1">
    <div class="cover__ring"></div>
    <h2 class="cover__title"><span class="cover__series">The Velvet Hour</span><span class="cover__name">Moonlit<br>Whispers</span></h2>
  </section>
  <section class="cover cover--grid cover--copper col-1 row-2">
    <div class="cover__ring"></div>
    <h2 class="cover__title"><span class="cover__series">The Copper</span><span class="cover__name">Table Evenings</span></h2>
  </section>
  <section class="cover cover--grid cover--silver col-2 row-2">
    <div class="cover__ring"></div>
    <h2 class="cover__title"><span class="cover__series">The Silver</span><span class="cover__name">Curtain Soirée</span></h2>
  </section>
  <section class="cover cover--grid cover--north col-3 row-2">
    <div class="cover__ring"></div>
    <h2 class="cover__title"><span class="cover__series">The Northwind</span><span class="cover__name">Orchestral<br>Treasures</span></h2>
  </section>
</main>
</body>
</html>
```